IT Company, Needs new Logo and Letterhead Design

We need a Letterhead and possible a new logo for an existing IT Company. We are not happy with our current Letterhead that we are using in our quotes etc. We are happy to change our logo if required. We will upload our current logo and letterhead and look forward to getting some examples. We provide Server, Workstation and network support.

Target Market(s)

Small to Medium Sized Businesses.

Industry/Entity Type

It Company

Requirements
Must have
• Ability to edit the letterhead at a later date. Will need the source files for editing once approved.
Nice to have
• Same colour scheme, but we are open to suggestions.

```html
<!DOCTYPE html>
<html lang="en">
<head>
<meta charset="utf-8">
<title>Tarvel Network Solutions Letterhead</title>
<link href="https://fonts.googleapis.com/css2?family=PT+Sans&display=swap" rel="stylesheet">
<style>
  :root {
    --canvas-bg: #e6e6e6;
    --sheet: #ffffff;
    --band: #e4e5e7;
    --ink: #333333;
    --ink-soft: #8a8a8a;
    --brand-grey: #6b6b6d;
    --brand-blue: #2f7fcf;
    --wash: #eef3f9;
    --wash-deep: #e8eef6;
  }
  html, body {
    margin: 0;
    width: 1200px;
    height: 1200px;
    overflow: hidden;
    background: var(--canvas-bg);
    font-family: "PT Sans", "Myriad Pro", sans-serif;
  }
  .letterhead {
    position: absolute;
    left: 222px;
    top: 68px;
    width: 754px;
    height: 1066px;
    background: var(--sheet);
    overflow: hidden;
  }
  .backdrop {
    position: absolute;
    inset: 0;
  }
  .header-band-left {
    position: absolute;
    left: 0;
    top: 49px;
    width: 16px;
    height: 81px;
    background: var(--band);
  }
  .header-band {
    position: absolute;
    left: 319px;
    top: 49px;
    width: 435px;
    height: 81px;
    background: var(--band);
  }
  .brand {
    position: absolute;
    left: 40px;
    top: 44px;
    display: flex;
    align-items: center;
    gap: 14px;
  }
  .brand-mark {
    width: 64px;
    height: 64px;
    border-radius: 50%;
    background: var(--brand-blue);
  }
  .brand-name {
    font-size: 24px;
    line-height: 1.05;
    color: var(--brand-grey);
    font-weight: 400;
  }
  .tagline {
    position: absolute;
    left: 375px;
    top: 82px;
    font-size: 14px;
    color: var(--ink);
  }
  .contact {
    position: absolute;
    left: 568px;
    top: 60px;
    font-size: 8.6px;
    line-height: 12.2px;
    color: var(--ink-soft);
  }
  .contact p { margin: 0; white-space: nowrap; }
</style>
</head>
<body>
  <main class="letterhead">
    <svg class="backdrop" width="754" height="1066" viewBox="0 0 754 1066" aria-hidden="true">
      <defs>
        <linearGradient id="wash" x1="0" y1="0" x2="0" y2="1">
          <stop offset="0" stop-color="#f6f8fb"/>
          <stop offset="1" stop-color="#f2f6fa"/>
        </linearGradient>
        <radialGradient id="bubble" cx="0.45" cy="0.45" r="0.6">
          <stop offset="0" stop-color="#ffffff"/>
          <stop offset="0.8" stop-color="#fbfbfc"/>
          <stop offset="1" stop-color="#f1f2f4"/>
        </radialGradient>
        <radialGradient id="orb" cx="0.5" cy="0.55" r="0.55">
          <stop offset="0" stop-color="#f3f6fa"/>
          <stop offset="1" stop-color="#eaeff6"/>
        </radialGradient>
      </defs>
      <rect class="wash" width="754" height="1066" fill="url(#wash)"/>
      <path class="wash-fade" d="M0 0 H754 V1066 H560 C680 1000 754 940 754 900 V0 Z" fill="none"/>
      <circle class="arc-white" cx="568" cy="90" r="390" fill="#ffffff"/>
      <circle class="orb-top" cx="570" cy="175" r="175" fill="url(#orb)"/>
      <circle class="orb-left" cx="75" cy="392" r="205" fill="url(#bubble)"/>
      <path class="sweep-lower" d="M754 960 C700 1010 630 1045 560 1066 H754 Z" fill="#ffffff"/>
      <rect width="754" height="1066" fill="none"/>
    </svg>

    <div class="header-band-left"></div>
    <div class="header-band"></div>

    <header class="brand">
      <span class="brand-mark"></span>
      <span class="brand-name">Tarvel<br>Network Solutions</span>
    </header>

    <p class="tagline">We are here to help!</p>

    <address class="contact">
      <p>PO BOX 2841, HARBOUR PLAZA, QLD 4612</p>
      <p>7 Wattle Street Coralbay,</p>
      <p>52 Banksia Street. Ferndale</p>
      <p>PHONE: 1300 482 615</p>
      <p>MOB: 0412 907 364</p>
    </address>
  </main>
</body>
</html>
```